Saving Lives with Dental Sleep Medicine

Looking for a brochure to market Dental Sleep Medicine educational courses . Whoever wins this bid will be hired to design the rest of our marketing campaign.
Design should be clean, simple with a modern feel. Not busy. Our courses utilize the most modern technology available.
Brochure content is attached, if you can't fit it all that is ok, we can tweak the content later. We are more focused on the look and feel of this design.
This brochure is marketing a 2 day course so there needs to be a spot for date, location, time & cost. As well as a notice of where to register VelmoraLearning.com, info@velmoralearning.com or call 1.800.###.#### and registration fees.
Also need a spot for Dr. Pelloquist's bio (attached). It's too long so just leave as much space as you can and we can amend the content.
Thank you so much. Looking forward to your designs. VelmEd Team :-)
Updates
Hello,
We are hoping for a minimalist design. Not busy. Clean and simple. We can reduce and minimize verbiage as needed. Just looking for layout and design.
Target Market(s)
Dentists
Requirements
Must have
- Clean lines, simple feel, minimalist and modern. Same font as logo. Black, white, gray.
Should not have
- Busy look and feel

```html
<!DOCTYPE html>
<html lang="en">
<head>
<meta charset="utf-8">
<title>Sleep &amp; Airway Management Brochure</title>
<link href="https://fonts.googleapis.com/css2?family=Source+Sans+3:wght@300;400;600&display=swap" rel="stylesheet">
<style>
:root{
  --coral:#e8606f;
  --ink:#5f5f68;
  --ink-dark:#44444c;
  --band:#c9c9d0;
  --paper:#f7f7f8;
  --stage:#e4e4e8;
  --photo-warm:#8a7466;
  --photo-cool:#b9bcc4;
}
*{box-sizing:border-box;margin:0;padding:0}
html,body{width:1200px;height:659px;overflow:hidden}
body{background:var(--stage);font-family:"Source Sans 3",sans-serif;color:var(--ink);position:relative}
.spread{position:absolute;top:131px;width:570px;height:396px;background:var(--paper);box-shadow:0 2px 8px rgba(0,0,0,.12);overflow:hidden}
.spread--inside{left:20px}
.spread--outside{left:610px}
.fold{position:absolute;top:0;bottom:0;width:1px;background:rgba(0,0,0,.06)}
.abs{position:absolute}
.photo{position:absolute;background:linear-gradient(135deg,var(--photo-warm),var(--photo-cool))}
.heading{font-weight:400;text-transform:uppercase;color:var(--ink);line-height:1}
.heading em{font-style:normal;color:var(--coral)}
.bullets{list-style:none}
.bullets li{position:relative;padding-left:18px;font-size:6.2px;line-height:1.25;padding-bottom:2.6px;margin-bottom:2.6px;border-bottom:.5px solid #dcdce0}
.bullets li::before{content:"";position:absolute;left:2px;top:1px;width:6px;height:6px;border-radius:50%;background:var(--coral)}
.bullets li::after{content:"";position:absolute;left:4px;top:2.8px;width:2px;height:2px;border-right:.8px solid #fff;border-top:.8px solid #fff;transform:rotate(45deg)}
.footer-band{position:absolute;left:0;right:0;bottom:0;height:26px;background:var(--band)}
.footer-url{position:absolute;font-size:5px;color:#fff}
.course-box{position:absolute;left:205px;top:28px;width:350px;height:152px;background:var(--coral);color:#fff;padding:14px 14px}
.course-box .heading{color:var(--ink-dark);font-size:14px;font-weight:600;line-height:1}
.course-text{font-size:5.5px;line-height:1.45;text-align:justify}
.col-left{position:absolute;left:14px;top:50px;width:152px}
.col-right{position:absolute;left:186px;top:12px;width:152px}
.col-right p+p{margin-top:6px}
.bio-name{position:absolute;left:20px;top:44px;font-size:9px;font-weight:600;color:var(--coral);line-height:1.15}
.bio-tab{position:absolute;left:0;top:44px;width:10px;height:20px;background:var(--coral)}
.bio-text{position:absolute;left:20px;top:104px;width:150px;font-size:4.4px;line-height:1.4;color:#77777f;text-align:justify}
.bio-text p+p{margin-top:4px}
.contact{position:absolute;left:210px;font-size:5px;display:flex;align-items:center;gap:5px}
.brand{position:absolute;left:380px;top:195px;width:190px;height:34px;background:#eeeef0;display:flex;align-items:center;justify-content:center;gap:6px;font-size:13px;font-weight:300;color:#8a8a92}
.brand-mark{width:10px;height:10px;background:var(--coral)}
.cover-box{position:absolute;left:372px;top:229px;width:183px;height:120px;background:var(--coral);color:#fff;padding:14px 12px}
.cover-title{font-size:16px;font-weight:600;line-height:1.22}
.cover-sub{font-size:6.4px;margin-top:10px;line-height:1.35}
.cover-grey{position:absolute;left:380px;top:349px;width:190px;height:47px;background:var(--band)}
</style>
</head>
<body>

<section class="spread spread--inside" aria-label="Brochure inside">
  <div class="fold" style="left:190px"></div>
  <div class="fold" style="left:380px"></div>

  <h2 class="heading abs" style="left:16px;top:26px;font-size:14px">Topics <em>covered:</em></h2>
  <ul class="bullets abs" style="left:12px;top:56px;width:165px">
    <li>Fundamentals of Sleep &amp; Sleep Disorders</li>
    <li>Understand Obstructive Sleep Apnea (OSA) &amp; Treatment Options</li>
    <li>How to Implement an effective Sleep Screening Protocol in a Dental Clinic</li>
    <li>Sleep Testing</li>
    <li>How to order an appliance for OAT</li>
    <li>Appliance Selection</li>
    <li>Importance of patient selection</li>
    <li>Overview of NOVRA Plus System</li>
    <li>Hands-on workshop for NOVRA Tray Fitting</li>
    <li>Hands-on workshop for Bite-Registration</li>
    <li>Technology &amp; Sleep</li>
    <li>Fully Digital Workflow for OAT</li>
    <li>NOVRA Plus Case Studies</li>
    <li>Medical Billing for OAT</li>
    <li>How to maximize the utilization of your NOVRA Plus at your clinic</li>
    <li>Simple and easy to follow clinical workflow</li>
  </ul>
  <div class="photo" role="img" aria-label="Photo of a group of dentists at a workshop in a clinic" style="left:14px;top:282px;width:164px;height:82px"></div>

  <div class="course-box">
    <h2 class="heading">Course<br>description:</h2>
    <p class="course-text col-left">Dental Sleep Medicine (DSM) has been growing rapidly over the past decade. Despite such growth, Oral Appliance Therapy (OAT) could be challenging in terms of predictability and workflow efficiency, resulting in many clinicians being reluctant to incorporate “Sleep &amp; OAT” into their clinics. However, most of these challenges can now be addressed by utilizing available technologies in healthcare industry; resulting in improved and predictable clinical</p>
    <div class="course-text col-right">
      <p>workflows, patient experience, quality of care and access to care.</p>
      <p>This program will review the importance of Sleep &amp; Airway Management in comprehensive inter-disciplinary treatment planning and how airway &amp; sleep disorders, if left untreated, could adversely impact the long-term prognosis of dental treatments. It will also provide a practical step-by-step guide for implementing a simple &amp; predictable “Sleep and Airway Management” program; utilizing easy to implement systems, improved patient communication &amp; education through intraoral scanning, &amp; 3D imaging AND a fully digital workflow for OAT.</p>
    </div>
  </div>

  <h2 class="heading abs" style="left:205px;top:200px;font-size:14px;line-height:1.05">Learning<br><em>objectives:</em></h2>
  <ul class="bullets abs" style="left:203px;top:240px;width:160px">
    <li>Step by step instruction on how to systematically integrate sleep into your practice</li>
    <li>Why dental clinics should have a comprehensive understanding of sleep &amp; airway disorders, and educate their patients</li>
    <li>How to implement a sleep and airway management program in a dental clinic</li>
    <li>Overview of some of the latest technologies in dentistry and how each could be utilized in Dental Sleep Medicine (DSM)</li>
  </ul>

  <div class="photo" role="img" aria-label="Photo of a presenter demonstrating to attendees around a dental chair" style="left:388px;top:198px;width:167px;height:84px"></div>
  <ul class="bullets abs" style="left:386px;top:294px;width:168px">
    <li>How to utilize your NOVRA Plus System effectively in your clinic</li>
    <li>Proper selection of oral appliances for OSA</li>
    <li>Medical Billing for OAT</li>
  </ul>

  <div class="footer-band"></div>
  <svg class="abs" style="left:0;top:370px" width="570" height="26" aria-hidden="true">
    <line x1="110" y1="12" x2="555" y2="6" stroke="var(--coral)" stroke-width="1.6"/>
  </svg>
  <span class="footer-url" style="left:16px;top:380px">velmoralearning.com</span>
</section>

<section class="spread spread--outside" aria-label="Brochure outside">
  <div class="fold" style="left:190px"></div>
  <div class="fold" style="left:380px"></div>

  <div class="bio-tab"></div>
  <h2 class="bio-name">Dr. Anselm<br>Pelloquist</h2>
  <div class="photo" role="img" aria-label="Round portrait photo of the course instructor" style="left:120px;top:20px;width:64px;height:64px;border-radius:50%"></div>
  <div class="bio-text">
    <p>Dr. Pelloquist received his Doctor of Dental Surgery degree and a Bachelor of Medical Sciences. He also earned fellowships in physiologic aesthetics and advanced dental studies, and completed a research fellowship in sleep and dental sleep medicine abroad.</p>
    <p>Dr. Pelloquist is a general dentist who maintains a group of private practices with a strong interest in dental sleep medicine and TMD management. He is actively involved in clinical research, and his work focuses on new technologies that improve treatment outcome, predictability and patient selection in oral appliance therapy.</p>
    <p>He is the founder and director of a regional dental sleep medicine study club and has trained hundreds of dentists in dental sleep medicine.</p>
  </div>
  <span class="footer-url" style="left:20px;top:374px;color:#8a8a92">velmoralearning.com</span>
  <svg class="abs" style="left:0;top:360px" width="380" height="20" aria-hidden="true">
    <line x1="80" y1="14" x2="190" y2="8" stroke="var(--coral)" stroke-width="1.6"/>
    <line x1="190" y1="8" x2="345" y2="10" stroke="var(--coral)" stroke-width="1.6"/>
  </svg>

  <div class="photo" role="img" aria-label="Photo of attendees gathered in a modern dental clinic" style="left:200px;top:55px;width:178px;height:160px"></div>

  <div class="contact" style="top:275px">
    <svg width="6" height="8" viewBox="0 0 6 8" aria-hidden="true"><path d="M3 0a3 3 0 0 1 3 3c0 2-3 5-3 5S0 5 0 3a3 3 0 0 1 3-3z" fill="var(--coral)"/><circle cx="3" cy="3" r="1" fill="#fff"/></svg>
    Ridgefield, Alberta, Canada
  </div>
  <div class="contact" style="top:293px">
    <svg width="7" height="7" viewBox="0 0 7 7" aria-hidden="true"><circle cx="3.5" cy="3.5" r="3.5" fill="var(--coral)"/><path d="M2.3 1.8l1 1-.5.6a3 3 0 0 0 1 1l.6-.5 1 1-.6.6C3.8 5.3 1.7 3.2 1.7 2.4z" fill="#fff"/></svg>
    1.800.###.####
  </div>
  <div class="contact" style="top:311px">
    <svg width="8" height="6" viewBox="0 0 8 6" aria-hidden="true"><rect width="8" height="6" fill="var(--coral)"/><path d="M0 0l4 3 4-3" fill="none" stroke="#fff" stroke-width=".7"/></svg>
    info@velmoralearning.com
  </div>

  <div class="photo" role="img" aria-label="Photo of the instructor presenting on stage" style="left:380px;top:0;width:190px;height:195px;background:linear-gradient(135deg,#d8d8dc,#3a3f5a)"></div>
  <div class="brand"><span class="brand-mark"></span>VelmoraLearning</div>
  <div class="cover-grey"></div>
  <div class="cover-box">
    <h1 class="cover-title">Sleep &amp; Airway<br>Management in<br>a Dental Clinic</h1>
    <p class="cover-sub">NOVRA Plus System &amp; Fully Digital<br>Workflows for OAT</p>
  </div>
</section>

</body>
</html>
```